Set of 6 Icons and buttons required

We have written a windows based app which gives clients access to reports etc.

We are a multichannel epos company

We require 6 buttons and icons along with a suggested font to use and a background for the form.

I have attatched a mock up of what we require from the chosen designer.

The buttons are as follows :

Stockcard ( This is a program which customers can enter stock and check stock levels etc )

Reports ( as the title says )

Stock ( This for making adjustments )

Goods ( this is for booking goods in )

Settings ( As title says )

Help ( As title says )

Dimensions
---------------

The form : 296x268
Buttons : 218x36
Icons on button : 32x32
Text size : Size 10

If you look at the attatched document this is something I put together just to show what we are looking once we put all the components together

Our website is q-ledgora.co.uk

Target Market(s)

B2B

Industry/Entity Type

It Company

```html
<!DOCTYPE html>
<html lang="en">
<head>
<meta charset="utf-8">
<title>q-ledgora — Main Menu</title>
<link href="https://fonts.googleapis.com/css2?family=Arimo:wght@400&display=swap" rel="stylesheet">
<style>
  :root {
    --canvas: #ffffff;
    --form-bg: #e3e3e1;
    --form-edge: #cfcfcd;
    --titlebar-top: #f6f6f5;
    --titlebar-bottom: #dededc;
    --close-top: #f2f2f2;
    --close-bottom: #c4c4c4;
    --close-glyph: #5a5a5a;
    --button-top: #ffffff;
    --button-mid: #f3f3f3;
    --button-bottom: #c9c9c9;
    --icon-top: #ffffff;
    --icon-bottom: #d4d4d4;
    --label: #6e6e6e;
    --brand-top: #2a1f5c;
    --brand-mid: #3b2f74;
    --brand-bottom: #2f6fb0;
    --brand-text: #ffffff;
    --green: #1a9a3a;
    --red: #d62020;
    --blue: #1f5fc2;
    --orange: #f08a1c;
  }
  html, body {
    margin: 0;
    width: 1200px;
    height: 1082px;
    overflow: hidden;
    background: var(--canvas);
    font-family: "Arimo", Arial, sans-serif;
  }
  .app-form {
    position: absolute;
    left: 0; top: 0;
    width: 1200px; height: 1082px;
    box-sizing: border-box;
    background: var(--form-bg);
    border: 2px solid var(--form-edge);
    border-radius: 14px;
    overflow: hidden;
  }
  .title-bar {
    position: absolute;
    left: 0; top: 0; right: 0;
    height: 127px;
    background: linear-gradient(var(--titlebar-top), var(--titlebar-bottom));
  }
  .close-button {
    position: absolute;
    left: 1047px; top: 29px;
    width: 87px; height: 77px;
    border-radius: 8px;
    background: linear-gradient(var(--close-top), var(--close-bottom));
    box-shadow: 0 1px 2px rgba(0,0,0,.25);
    display: flex; align-items: center; justify-content: center;
  }
  .brand-panel {
    position: absolute;
    left: 36px; top: 226px;
    width: 226px; height: 762px;
    background: linear-gradient(var(--brand-top) 0%, var(--brand-mid) 60%, var(--brand-bottom) 100%);
  }
  .brand-name {
    position: absolute;
    left: 0; right: 0; bottom: 40px;
    text-align: center;
    color: var(--brand-text);
    font-size: 34px;
    line-height: 1;
  }
  .menu {
    position: absolute;
    left: 291px; top: 217px;
    width: 871px;
    margin: 0; padding: 0;
    list-style: none;
  }
  .menu-button {
    position: relative;
    height: 127px;
    margin-bottom: 3px;
    border-radius: 12px;
    background: linear-gradient(var(--button-top) 0%, var(--button-mid) 45%, var(--button-bottom) 100%);
    display: flex; align-items: center;
  }
  .menu-icon {
    width: 111px; height: 99px;
    margin-left: 21px;
    border-radius: 10px;
    background: linear-gradient(var(--icon-top), var(--icon-bottom));
    display: flex; align-items: center; justify-content: center;
  }
  .menu-label {
    margin-left: 40px;
    font-size: 49px;
    color: var(--label);
    letter-spacing: .5px;
  }
</style>
</head>
<body>
<div class="app-form">
  <div class="title-bar">
    <div class="close-button" aria-label="Close">
      <svg width="44" height="44" viewBox="0 0 44 44"><path d="M6 6 L38 38 M38 6 L6 38" stroke="var(--close-glyph)" stroke-width="10"/></svg>
    </div>
  </div>

  <div class="brand-panel" role="img" aria-label="Brand panel with product name">
    <span class="brand-name">q-ledgora</span>
  </div>

  <ul class="menu">
    <li class="menu-button">
      <span class="menu-icon">
        <svg width="80" height="72" viewBox="0 0 80 72">
          <g fill="var(--green)">
            <rect x="14" y="52" width="9" height="14"/><rect x="27" y="44" width="9" height="22"/>
            <rect x="40" y="36" width="9" height="30"/><rect x="53" y="28" width="9" height="38"/>
            <rect x="66" y="20" width="9" height="46"/>
          </g>
          <polyline points="4,40 20,26 30,32 46,16 58,12" fill="none" stroke="var(--red)" stroke-width="3"/>
          <polygon points="70,4 56,6 62,16" fill="var(--red)"/>
        </svg>
      </span>
      <span class="menu-label">Stockcard</span>
    </li>
    <li class="menu-button">
      <span class="menu-icon">
        <svg width="60" height="76" viewBox="0 0 60 76">
          <polygon points="6,18 22,2 54,2 54,74 6,74" fill="var(--blue)"/>
          <polygon points="6,18 22,2 22,18" fill="#9ad35a"/>
          <g fill="#ffffff"><rect x="14" y="28" width="32" height="4"/><rect x="14" y="38" width="32" height="4"/><rect x="14" y="48" width="32" height="4"/><rect x="14" y="58" width="32" height="4"/></g>
        </svg>
      </span>
      <span class="menu-label">Reports</span>
    </li>
    <li class="menu-button">
      <span class="menu-icon">
        <svg width="80" height="66" viewBox="0 0 80 66">
          <g fill="var(--green)">
            <rect x="6" y="48" width="11" height="16"/><rect x="21" y="38" width="11" height="26"/>
            <rect x="36" y="28" width="11" height="36"/><rect x="51" y="16" width="11" height="48"/>
            <rect x="66" y="4" width="11" height="60"/>
          </g>
        </svg>
      </span>
      <span class="menu-label">Stock</span>
    </li>
    <li class="menu-button">
      <span class="menu-icon">
        <svg width="76" height="66" viewBox="0 0 76 66">
          <polyline points="4,8 16,8 26,44 62,44" fill="none" stroke="var(--orange)" stroke-width="5" stroke-linejoin="round"/>
          <polygon points="18,12 72,12 62,38 26,38" fill="#3a3a3a"/>
          <circle cx="30" cy="56" r="6" fill="#2a8ad6"/><circle cx="58" cy="56" r="6" fill="#2a8ad6"/>
        </svg>
      </span>
      <span class="menu-label">Goods</span>
    </li>
    <li class="menu-button">
      <span class="menu-icon">
        <svg width="72" height="72" viewBox="0 0 72 72">
          <g transform="translate(26 26)" fill="var(--red)">
            <circle r="15"/>
            <g><rect x="-5" y="-23" width="10" height="10"/><rect x="-5" y="13" width="10" height="10"/><rect x="-23" y="-5" width="10" height="10"/><rect x="13" y="-5" width="10" height="10"/></g>
            <g transform="rotate(45)"><rect x="-5" y="-23" width="10" height="10"/><rect x="-5" y="13" width="10" height="10"/><rect x="-23" y="-5" width="10" height="10"/><rect x="13" y="-5" width="10" height="10"/></g>
            <circle r="6" fill="#e8e8e8"/>
          </g>
          <g transform="translate(54 54)" fill="var(--green)">
            <circle r="9"/>
            <g><rect x="-3" y="-14" width="6" height="6"/><rect x="-3" y="8" width="6" height="6"/><rect x="-14" y="-3" width="6" height="6"/><rect x="8" y="-3" width="6" height="6"/></g>
            <g transform="rotate(45)"><rect x="-3" y="-14" width="6" height="6"/><rect x="-3" y="8" width="6" height="6"/><rect x="-14" y="-3" width="6" height="6"/><rect x="8" y="-3" width="6" height="6"/></g>
            <circle r="3.5" fill="#e8e8e8"/>
          </g>
        </svg>
      </span>
      <span class="menu-label">Settings</span>
    </li>
    <li class="menu-button">
      <span class="menu-icon">
        <svg width="70" height="70" viewBox="0 0 70 70">
          <circle cx="35" cy="35" r="26" fill="none" stroke="#ffffff" stroke-width="14"/>
          <circle cx="35" cy="35" r="26" fill="none" stroke="var(--red)" stroke-width="14" stroke-dasharray="20.4 20.4" stroke-dashoffset="10.2"/>
          <circle cx="35" cy="35" r="33" fill="none" stroke="#999" stroke-width="1.5"/>
          <circle cx="35" cy="35" r="19" fill="none" stroke="#999" stroke-width="1.5"/>
        </svg>
      </span>
      <span class="menu-label">Help</span>
    </li>
  </ul>
</div>
</body>
</html>
```